Qorva - Web Design Rebrand for Talent Resourcing Company

I need a new brand for a customer based in Ireland.
The website currently: https://braddick.io/
Braddick repositioning themselves to be strategic talent resourcing and operational technology consultancy, Specialising in Life Sciences and Data Centres.
Essentially their USP:
They have lots of specialist manufacturing & automation resources that understand the Life Sciences Industry

Competitor websites:
https://vernhollow.com/ I really like the clarity on this site and the pink/yellow mix could be replaced with a green/blue mix for Braddick?
https://tulimark.com/ These are a big company so anything we could steal would be good 😊

They want:
• Fresh, sharp imagery
• Movement on the main page (Margot is obsessed with this lol) so may be video on some sections?
• The facility to upload CVs so similar to above.
• A page to show types of jobs available
• A page to show types of resource available from Braddick
• About us
• Sectors they operate in (includes Life Sciences, Food & Bev, Data Centres)

Target Market(s)

HR/Recruitment/Talent Acquisition/Operations Personnel in Life Sciences and Data Centres

Industry/Entity Type

Life Sciences and Data Centres

Number of Pages Required

1 page

Font styles to use
Sans Serif

Colors
0054AA
0677BA
7BADD7
CADEEF
E8F1F8
0094D4
00A9DD
6FCCEA
C7EBF8
E9F6FB
00AB8E
00BBA5
67D7C9
C6EFE9
E9F9F6

Requirements
Must have
• Brand Colour might be green/blue mix OR if another colour combo compelling
Nice to have
• Fresh, Sharp imagery. Movement on the main image (maybe partial video)

```html
<!DOCTYPE html>
<html lang="en">
<head>
<meta charset="utf-8">
<title>Braddick – Strategic Talent Resourcing</title>
<link href="https://fonts.googleapis.com/css2?family=Open+Sans:wght@400;600;700;800&family=Roboto+Slab:wght@500;600;700&display=swap" rel="stylesheet">
<style>
:root{
  --navy:#0054AA; --blue:#0677BA; --sky:#7BADD7; --pale:#CADEEF; --mist:#E8F1F8;
  --cyan:#0094D4; --cyan2:#00A9DD; --aqua:#6FCCEA;
  --teal:#00AB8E; --teal2:#00BBA5; --mint:#67D7C9; --mintpale:#C6EFE9;
  --ink:#222b33; --text:#3c4650; --muted:#7a8590; --line:#d9e1e8; --white:#fff;
}
*{box-sizing:border-box;margin:0;padding:0}
html,body{width:1200px;height:4252px;overflow:hidden}
body{font-family:"Open Sans",sans-serif;color:var(--text);background:#fff;position:relative}
h1,h2,h3,h4{font-family:"Roboto Slab",serif;color:var(--ink);font-weight:600}
.wrap{width:1076px;margin:0 auto;position:relative}
.btn{display:inline-block;font-weight:600;border-radius:3px;text-decoration:none}
.section-title{text-align:center;font-size:34px}

/* top bar */
.topbar{height:36px;background:var(--teal);color:#fff;font-size:10px}
.topbar .wrap{display:flex;justify-content:space-between;align-items:center;height:36px}
.topbar .info{display:flex;gap:14px;align-items:center}
.topbar .info span{display:flex;gap:4px;align-items:center}
.social{display:flex;gap:6px}
.social i{width:20px;height:20px;border:1px solid #fff;border-radius:50%;display:block}

/* hero */
.hero{height:545px;position:relative;overflow:hidden}
.hero-bg{position:absolute;inset:0;background:radial-gradient(circle at 70% 60%,#3f6f78 0,#20444c 40%,#122a31 100%)}
.hero-bg::after{content:"";position:absolute;inset:0;background:linear-gradient(180deg,rgba(0,0,0,.25),rgba(0,60,70,.35))}
.nav{position:relative;z-index:2;height:70px;display:flex;align-items:center;justify-content:space-between}
.logo{font-family:"Open Sans",sans-serif;font-weight:800;font-size:40px;color:#fff;letter-spacing:-.5px}
.menu{display:flex;gap:42px;align-items:center;font-size:13px;color:#fff;font-weight:600}
.hero-copy{position:relative;z-index:2;text-align:center;margin-top:100px}
.hero-copy h1{font-size:40px;color:#fff;line-height:1.15;font-weight:600}
.hero-copy h1 em{font-style:normal;color:var(--aqua)}
.hero-copy p{color:#fff;font-size:18px;margin:12px 0 26px}
.hero-copy .btn{background:var(--teal);color:#fff;font-size:18px;padding:9px 18px}

/* sectors */
.sectors{height:231px;padding-top:60px}
.sectors .wrap{display:flex}
.sector{flex:1;padding:0 14px 0 0;border-right:1px solid var(--line);margin-right:28px}
.sector:last-child{border:0;margin:0}
.sector-head{display:flex;align-items:center;gap:14px}
.sector-icon{width:60px;height:60px;border-radius:50%;background:var(--mist);display:flex;align-items:center;justify-content:center}
.sector h3{font-size:24px}
.sector p{font-size:13px;line-height:1.3;margin:12px 0 0 92px;color:var(--ink)}

/* about */
.about{height:555px;background:var(--mist);position:relative}
.about-photo{position:absolute;left:104px;top:98px;width:356px;height:356px;border-radius:50%;background:linear-gradient(160deg,var(--sky),#5a8fc2)}
.dot-sm{position:absolute;left:430px;top:98px;width:22px;height:22px;border-radius:50%;background:var(--cyan)}
.dot-lg{position:absolute;left:154px;top:464px;width:48px;height:48px;border-radius:50%;background:var(--cyan)}
.about-copy{position:absolute;left:543px;top:64px;width:592px}
.eyebrow{font-size:13px;color:var(--teal);font-weight:600}
.about-copy h2{font-size:34px;margin:8px 0 14px}
.about-copy .lead{font-family:"Roboto Slab",serif;font-size:20px;line-height:1.28;color:var(--ink);margin-bottom:26px}
.about-copy p{font-size:12.5px;line-height:1.35;color:var(--ink);margin-bottom:14px}
.about-copy .btn{background:var(--teal);color:#fff;font-size:18px;padding:8px 18px;margin-top:30px}

/* jobs */
.jobs{height:527px;padding-top:48px}
.job-grid{display:flex;gap:17px;margin-top:30px}
.job{width:256px;height:292px;background:#fff;box-shadow:0 2px 14px rgba(0,40,80,.12);border-radius:4px;padding:22px 12px 0}
.job-head{display:flex;gap:8px}
.job-icon{width:44px;height:44px;border-radius:6px;background:var(--mist)}
.job h4{font-size:14px;font-weight:600}
.job .meta{font-size:9px;color:var(--muted);margin-top:4px;display:flex;gap:10px}
.job .desc{font-size:10px;line-height:1.25;margin-top:12px;color:var(--text)}
.tags{display:flex;flex-wrap:wrap;gap:10px 8px;margin-top:16px;width:200px}
.tag{font-size:10px;padding:4px 10px;background:#f1f4f7;border-radius:3px}
.job-foot{display:flex;justify-content:space-between;align-items:center;margin-top:36px;padding:0 2px}
.price{font-size:18px;font-weight:700;color:var(--ink)}
.price small{font-size:11px;font-weight:400;color:var(--muted)}
.job-foot .btn{background:var(--navy);color:#fff;font-size:11px;padding:8px 20px}
.pager{display:flex;justify-content:center;gap:5px;margin-top:60px}
.pager i{width:7px;height:7px;border-radius:50%;background:var(--pale);display:block}
.pager i:first-child{width:16px;border-radius:4px;background:var(--cyan)}

/* upload */
.upload{height:227px;background:var(--teal);padding-top:22px}
.upload h2{color:#fff;font-size:34px;text-align:center}
.cv-form{display:flex;gap:24px;margin-top:26px;align-items:flex-end;padding:0 20px}
.field label{display:block;color:#fff;font-size:13px;font-weight:600;margin-bottom:8px}
.field label b{color:#ff6b6b}
.field .input{width:342px;height:50px;border:1px solid #fff;border-radius:3px;color:#fff;font-size:13px;font-weight:600;padding:16px 12px}
.upload .btn-up{background:var(--navy);color:#fff;font-size:13px;padding:17px 29px}
.upload .btn-sub{background:var(--mint);color:var(--navy);font-size:13px;padding:17px 30px;margin-left:-10px}

/* resources */
.resources{height:438px;padding-top:60px}
.res-grid{display:grid;grid-template-columns:repeat(3,341px);gap:24px 26px;margin-top:40px}
.res{height:110px;border:1px solid #cfd7de;border-radius:4px;display:flex;align-items:center;gap:14px;padding:0 14px}
.res-icon{width:84px;height:84px;background:var(--mist)}
.res h4{font-size:19px}
.res span{font-size:10px;color:var(--muted);display:block;margin-top:6px}

/* stats */
.stats{height:206px;background:var(--cyan)}
.stats .wrap{display:flex;justify-content:space-around;padding-top:44px}
.stat{text-align:center;color:#fff;width:300px}
.stat strong{font-family:"Open Sans",sans-serif;font-size:64px;font-weight:800;display:block;line-height:1}
.stat span{font-size:19px;font-weight:600;color:var(--mintpale);display:block;margin-top:6px;line-height:1.15}

/* team */
.team{height:608px;background:var(--mist);padding-top:22px;text-align:center}
.team .intro{font-size:13px;color:var(--ink);line-height:1.35;width:800px;margin:18px auto 0}
.team .intro p{margin-bottom:8px}
.team-row{display:flex;gap:30px;justify-content:center;margin-top:26px;position:relative}
.member{width:265px;height:380px;background:#fff;border-radius:4px;overflow:hidden}
.member .photo{height:297px;background:linear-gradient(180deg,#eceff2,#c9d2da)}
.member h4{font-size:22px;margin-top:14px}
.member span{font-size:11px;color:var(--muted)}
.arrow{position:absolute;top:170px;width:32px;height:32px;background:var(--cyan);border-radius:3px;display:flex;align-items:center;justify-content:center}
.arrow.prev{left:130px}.arrow.next{right:130px}

/* featured */
.featured{height:551px;padding-top:56px}
.feat-grid{display:flex;gap:25px;margin-top:32px}
.feat{width:342px;height:376px;box-shadow:0 2px 14px rgba(0,40,80,.1);border-radius:4px;position:relative}
.feat .img{height:244px}
.feat .go{position:absolute;right:30px;top:220px;width:46px;height:46px;border-radius:50%;background:var(--cyan);border:3px solid #fff;display:flex;align-items:center;justify-content:center}
.feat h4{font-size:21px;margin:36px 20px 10px}
.feat p{font-size:10px;line-height:1.25;margin:0 20px;color:var(--text)}

/* footer */
.footer{height:269px;background:var(--navy);color:#fff;padding-top:36px}
.footer .wrap{display:flex}
.f-about{width:380px}
.f-about .logo{font-size:40px}
.f-about p{font-size:13px;line-height:1.3;margin:14px 0 18px}
.f-col h4{color:#fff;font-size:20px;font-weight:500}
.f-col h4::after{content:"";display:block;width:34px;height:2px;background:var(--mint);margin:14px 0 18px}
.f-col ul{list-style:none;font-size:12px;line-height:22.5px}
.f-col.info{width:248px}.f-col.svc{width:218px}
.f-col .ho{font-weight:700;font-size:15px;margin-bottom:4px}
.f-col .row{display:flex;gap:6px;align-items:flex-start;font-size:13px;line-height:20px}
.copyright{height:59px;background:#02428a;color:#fff;font-size:13px;text-align:center;line-height:59px}
</style>
</head>
<body>

<div class="topbar">
  <div class="wrap">
    <div class="info">
      <span><svg width="8" height="11" viewBox="0 0 8 11"><path d="M4 0a4 4 0 0 0-4 4c0 3 4 7 4 7s4-4 4-7a4 4 0 0 0-4-4zm0 5.5A1.5 1.5 0 1 1 4 2.5a1.5 1.5 0 0 1 0 3z" fill="#fff"/></svg>Harbour Row, Ballyrenn, Co. Cork, T45 R210</span>
      <span><svg width="10" height="10" viewBox="0 0 10 10"><path d="M2 0l2 2.5-1 1.3a6 6 0 0 0 3.2 3.2l1.3-1L10 8l-1.3 2C4 10 0 6 0 1.3z" fill="#fff"/></svg>+353 21 555 0187</span>
    </div>
    <div class="social"><i></i><i></i></div>
  </div>
</div>

<header class="hero">
  <div class="hero-bg" role="img" aria-label="Engineer holding a tablet with glowing data charts in a dark control room"></div>
  <div class="wrap nav">
    <div class="logo">Braddick</div>
    <nav class="menu">
      <span>ABOUT US</span><span>CAPABILITIES</span><span>OUR CLIENTS</span><span>JOIN OUR TEAM</span><span>CONTACT</span>
      <svg width="14" height="14" viewBox="0 0 14 14"><circle cx="6" cy="6" r="4.5" stroke="#fff" stroke-width="2" fill="none"/><path d="M9.5 9.5L13 13" stroke="#fff" stroke-width="2"/></svg>
    </nav>
  </div>
  <div class="hero-copy">
    <h1>Strategic Talent Resourcing and<br><em>Operational Technology Experts</em></h1>
    <p>Specialising in Life Sciences and Data Centres.</p>
    <a class="btn">Contact Us</a>
  </div>
</header>

<section class="sectors">
  <div class="wrap">
    <div class="sector">
      <div class="sector-head"><div class="sector-icon"><svg width="34" height="34" viewBox="0 0 34 34" fill="none" stroke="#00AB8E" stroke-width="2"><path d="M12 4h10M14 4v10L6 28a2 2 0 0 0 2 3h18a2 2 0 0 0 2-3l-8-14V4"/></svg></div><h3>Life Sciences</h3></div>
      <p>Lorem Ipsum is simply dummy text of the printing and typesetting industry. Lorem Ipsum has been...</p>
    </div>
    <div class="sector">
      <div class="sector-head"><div class="sector-icon"><svg width="34" height="34" viewBox="0 0 34 34" fill="none" stroke="#00AB8E" stroke-width="2"><path d="M5 16h24M7 16a10 10 0 0 1 20 0M6 22h22l-2 6H8z"/></svg></div><h3>Food &amp; Bev</h3></div>
      <p>Lorem Ipsum is simply dummy text of the printing and typesetting industry. Lorem Ipsum has been...</p>
    </div>
    <div class="sector">
      <div class="sector-head"><div class="sector-icon"><svg width="34" height="34" viewBox="0 0 34 34" fill="none" stroke="#00AB8E" stroke-width="2"><rect x="6" y="5" width="22" height="7"/><rect x="6" y="14" width="22" height="7"/><rect x="6" y="23" width="22" height="7"/></svg></div><h3>Data Centres</h3></div>
      <p>Lorem Ipsum is simply dummy text of the printing and typesetting industry. Lorem Ipsum has been...</p>
    </div>
  </div>
</section>

<section class="about">
  <div class="about-photo" role="img" aria-label="Smiling professional woman holding an open laptop"></div>
  <span class="dot-sm"></span><span class="dot-lg"></span>
  <div class="about-copy">
    <div class="eyebrow">ABOUT US</div>
    <h2>Welcome</h2>
    <p class="lead">Braddick is proud to be providing top-tier resources to the life sciences sector, specialising in delivering high-quality talent and solutions that enhance the capabilities and operational excellence of our customers.</p>
    <p>Ouroperational technology expertise and talent pool has evolved over the past decade with successful project delivery for numerous life sciences organisations, so we are uniquely positioned to understand and meet your requirements.</p>
    <p>We are focused on matching the dynamic needs of life sciences firms with skilled professionals, thereby driving innovation and growth in this critical sector across Ireland.</p>
    <a class="btn">Read more</a>
  </div>
</section>

<section class="jobs">
  <div class="wrap">
    <h2 class="section-title">Jobs Available</h2>
    <div class="job-grid">
      <article class="job">
        <div class="job-head"><div class="job-icon"></div><div><h4>Lorem Ipsum is simply...</h4><div class="meta"><span>Fulltime</span><span>4Minutes ago</span></div></div></div>
        <p class="desc">Lorem Ipsum is simply dummy text of the printing and typesetting industry. Lorem Ipsum has been the industry's standard dummy text ever since the 1500s...</p>
        <div class="tags"><span class="tag">Lorem</span><span class="tag">Dummy text</span><span class="tag">Simply dummy text</span></div>
        <div class="job-foot"><span class="price">$800<small>/Month</small></span><a class="btn">Apply now</a></div>
      </article>
      <article class="job">
        <div class="job-head"><div class="job-icon"></div><div><h4>Lorem Ipsum is simply...</h4><div class="meta"><span>Fulltime</span><span>4Minutes ago</span></div></div></div>
        <p class="desc">Lorem Ipsum is simply dummy text of the printing and typesetting industry. Lorem Ipsum has been the industry's standard dummy text ever since the 1500s...</p>
        <div class="tags"><span class="tag">Lorem</span><span class="tag">Dummy text</span><span class="tag">simply dummy text</span></div>
        <div class="job-foot"><span class="price">$800<small>/Month</small></span><a class="btn">Apply now</a></div>
      </article>
      <article class="job">
        <div class="job-head"><div class="job-icon"></div><div><h4>Lorem Ipsum is simply...</h4><div class="meta"><span>Fulltime</span><span>4Minutes ago</span></div></div></div>
        <p class="desc">Lorem Ipsum is simply dummy text of the printing and typesetting industry. Lorem Ipsum has been the industry's standard dummy text ever since the 1500s...</p>
        <div class="tags"><span class="tag">Lorem</span><span class="tag">Dummy text</span><span class="tag">simply dummy text</span></div>
        <div class="job-foot"><span class="price">$800<small>/Month</small></span><a class="btn">Apply now</a></div>
      </article>
      <article class="job">
        <div class="job-head"><div class="job-icon"></div><div><h4>Lorem Ipsum is simply...</h4><div class="meta"><span>Fulltime</span><span>4Minutes ago</span></div></div></div>
        <p class="desc">Lorem Ipsum is simply dummy text of the printing and typesetting industry. Lorem Ipsum has been the industry's standard dummy text ever since the 1500s...</p>
        <div class="tags"><span class="tag">Lorem</span><span class="tag">Dummy text</span><span class="tag">simply dummy text</span></div>
        <div class="job-foot"><span class="price">$800<small>/Month</small></span><a class="btn">Apply now</a></div>
      </article>
    </div>
    <div class="pager"><i></i><i></i><i></i></div>
  </div>
</section>

<section class="upload">
  <div class="wrap">
    <h2>Upload CVS</h2>
    <form class="cv-form">
      <div class="field"><label>Full Name<b>*</b></label><div class="input">Full Name</div></div>
      <div class="field"><label>Email address<b>*</b></label><div class="input">Email address</div></div>
      <div class="field"><label>Upload your CV</label><a class="btn btn-up">UPLOAD RESUME</a></div>
      <a class="btn btn-sub">SUBMIT</a>
    </form>
  </div>
</section>

<section class="resources">
  <div class="wrap">
    <h2 class="section-title">Resource Available</h2>
    <div class="res-grid">
      <div class="res"><div class="res-icon"></div><div><h4>Accounting / Finance</h4><span>5 Open Person</span></div></div>
      <div class="res"><div class="res-icon"></div><div><h4>Marketing</h4><span>10 Open Person</span></div></div>
      <div class="res"><div class="res-icon"></div><div><h4>Designer</h4><span>15 Open Person</span></div></div>
      <div class="res"><div class="res-icon"></div><div><h4>Developer</h4><span>24 Open Person</span></div></div>
      <div class="res"><div class="res-icon"></div><div><h4>Human Resource</h4><span>13 Open Person</span></div></div>
      <div class="res"><div class="res-icon"></div><div><h4>Project Manager</h4><span>20 Open Person</span></div></div>
    </div>
  </div>
</section>

<section class="stats">
  <div class="wrap">
    <div class="stat"><strong>50+</strong><span>Number skilled automation engineers</span></div>
    <div class="stat"><strong>25+</strong><span>Customers currently using Braddick</span></div>
    <div class="stat"><strong>99%</strong><span>Customer retention</span></div>
  </div>
</section>

<section class="team">
  <div class="wrap">
    <h2 class="section-title">Meet our Team</h2>
    <div class="intro">
      <p>Braddick employees have a variety of skills and experience, but they all are professional, experienced in their field and enjoy the variety of working at different client sites over time.</p>
      <p>They get a feeling of success seeing a project through to completion, and are always willing to go the extra mile for our clients.</p>
    </div>
    <div class="team-row">
      <div class="arrow prev"><svg width="14" height="12" viewBox="0 0 14 12"><path d="M13 6H2M6 1L1 6l5 5" stroke="#fff" stroke-width="2" fill="none"/></svg></div>
      <div class="member"><div class="photo" role="img" aria-label="Portrait of a team member in a dark blazer, arms crossed"></div><h4>Conor Lydon</h4><span>Developer</span></div>
      <div class="member"><div class="photo" role="img" aria-label="Portrait of a team member in a light blue blouse"></div><h4>Aisling Murray</h4><span>Developer</span></div>
      <div class="member"><div class="photo" role="img" aria-label="Portrait of a team member in a blue shirt, arms crossed"></div><h4>Ravi Desmond</h4><span>Developer</span></div>
      <div class="arrow next"><svg width="14" height="12" viewBox="0 0 14 12"><path d="M1 6h11M8 1l5 5-5 5" stroke="#fff" stroke-width="2" fill="none"/></svg></div>
    </div>
  </div>
</section>

<section class="featured">
  <div class="wrap">
    <h2 class="section-title">Featured</h2>
    <div class="feat-grid">
      <article class="feat"><div class="img" role="img" aria-label="Hands at a laptop with floating digital document icons" style="background:linear-gradient(135deg,#2b4d7a,#6c8fb8)"></div><span class="go"><svg width="16" height="14" viewBox="0 0 16 14"><path d="M1 7h13M8 1l6 6-6 6" stroke="#fff" stroke-width="2" fill="none"/></svg></span><h4>Automation &amp; csv</h4><p>Lorem Ipsum is simply dummy text of the printing and typesetting industry. Lorem Ipsum has been the industry's standard dummy text ever since the 1500s...</p></article>
      <article class="feat"><div class="img" role="img" aria-label="Seedling in soil with scientific hexagon icons" style="background:linear-gradient(135deg,#4a3a26,#9b7a48)"></div><span class="go"><svg width="16" height="14" viewBox="0 0 16 14"><path d="M1 7h13M8 1l6 6-6 6" stroke="#fff" stroke-width="2" fill="none"/></svg></span><h4>Bioprocess</h4><p>Lorem Ipsum is simply dummy text of the printing and typesetting industry. Lorem Ipsum has been the industry's standard dummy text ever since the 1500s...</p></article>
      <article class="feat"><div class="img" role="img" aria-label="Colleagues meeting around a table in a bright office" style="background:linear-gradient(135deg,#d9e2ec,#7a8da3)"></div><span class="go"><svg width="16" height="14" viewBox="0 0 16 14"><path d="M1 7h13M8 1l6 6-6 6" stroke="#fff" stroke-width="2" fill="none"/></svg></span><h4>Communication &amp; validation</h4><p>Lorem Ipsum is simply dummy text of the printing and typesetting industry. Lorem Ipsum has been the industry's standard dummy text ever since the 1500s...</p></article>
    </div>
  </div>
</section>

<footer class="footer">
  <div class="wrap">
    <div class="f-about">
      <div class="logo">Braddick</div>
      <p>Braddick is proud to be providing top-tier resources to the life sciences sector, specialising in delivering high-quality talent and solutions that enhan...</p>
      <div class="social"><i></i><i></i></div>
    </div>
    <div class="f-col info"><h4>Information</h4><ul><li>About Us</li><li>Capabilities</li><li>Our Clients</li><li>Join Our Team</li><li>Contact</li></ul></div>
    <div class="f-col svc"><h4>Services</h4><ul><li>Web Design</li><li>App Developemnt</li><li>Cloud Services</li><li>Domain Adn Hosting</li><li>Seo Optimization</li><li>Social Media</li></ul></div>
    <div class="f-col"><h4>Contact Us</h4>
      <div class="ho">Head Office</div>
      <div class="row"><svg width="10" height="10" viewBox="0 0 10 10" style="margin-top:5px"><path d="M2 0l2 2.5-1 1.3a6 6 0 0 0 3.2 3.2l1.3-1L10 8l-1.3 2C4 10 0 6 0 1.3z" fill="#fff"/></svg>+353 21 555 0187</div>
      <div class="row"><svg width="12" height="10" viewBox="0 0 12 10" style="margin-top:5px"><rect x=".5" y=".5" width="11" height="9" fill="none" stroke="#fff"/><path d="M.5 .5l5.5 5 5.5-5" fill="none" stroke="#fff"/></svg>info@braddick.io</div>
      <div class="row"><svg width="8" height="11" viewBox="0 0 8 11" style="margin-top:4px"><path d="M4 0a4 4 0 0 0-4 4c0 3 4 7 4 7s4-4 4-7a4 4 0 0 0-4-4z" fill="#fff"/></svg>Harbour Row, Ballyrenn,<br>Co. Cork, T45 R210</div>
    </div>
  </div>
</footer>
<div class="copyright">© 2024 Braddick. All Rights Reserved.</div>

</body>
</html>
```